Managed Service Provider VOIP Flyer

Looking for a one page US letter size single or double sided brochure to offer cloud hosted VoIP Phone system and unified communications. We have partnered with a VoIP Phone system company and want to sell their services but we don't want their name to be shown on the brochure because customers might call them directly. The company name is Quorvel (www.quorvel-example.com) and our company name is Lumen By Harlow, LLC and our voice product is called Clearly Talk. I have also uploaded my company's logo that you should show on the brochure and use that coloring. For more details about the product, you can visit their website mentioned above. Also I am looking for something very similar to this project and many of the technical details are the same https://flyer.contestpad-example.com/contest/5817264

I have also uploaded a PDF with my different package levels and some of the included features. Depending on the design we may or may not want the package levels on this flyer.

Target Market(s)

Small and medium Businesses

Industry/Entity Type

Voip

Requirements
Must have
• Feature and benefits information of Managed VOICE. Use my logo and coloring from my logo. Include our website, email, phone and possibly facebook if it makes sense/looks good.

www.lumenbyharlow-example.com
415.836.0.917
sales@lumenbyharlow-example.com
www.socialsite-example.com/lumenbyharlow
Nice to have
• Would like to show how the service is simple and reliable and available for any business size

```html
<!DOCTYPE html>
<html lang="en">
<head>
<meta charset="utf-8">
<title>Clearly Talk – Cloud Communications Flyer</title>
<link href="https://fonts.googleapis.com/css2?family=Roboto:wght@400;500;700&display=swap" rel="stylesheet">
<style>
:root{
  --navy:#0d2d5e;
  --red:#d8262f;
  --blue:#0b6ac2;
  --blue-mid:#0a539c;
  --blue-dark:#0a3a70;
  --ink:#1d1d1f;
  --grey-cell:#e4e5e8;
  --bg:#e6e6e6;
  --white:#ffffff;
}
*{box-sizing:border-box;margin:0;padding:0}
html,body{width:1200px;height:900px;overflow:hidden;background:var(--bg);font-family:'Roboto',Arial,sans-serif;color:var(--ink)}
.page{position:absolute;top:107px;width:530px;height:686px;background:var(--white);overflow:hidden}
.page--front{left:57px}
.page--back{left:613px}
.abs{position:absolute}

/* brand */
.brand{display:flex;align-items:center;gap:8px;color:var(--navy);font-weight:700;letter-spacing:.5px}
.brand__mark{background:var(--red);display:block}
.front-brand{left:0;width:530px;top:0;height:82px;justify-content:center;font-size:20px}
.front-brand .brand__mark{width:26px;height:26px}

/* hero */
.hero{left:0;top:82px;width:530px;height:126px;background:radial-gradient(ellipse at 70% 110%,#6b6a5e 0%,#3a4152 35%,#1b2233 70%,#10151f 100%)}
.hero__title{left:22px;top:98px;font-size:36px;font-weight:700;color:var(--white)}
.hero__sub{left:22px;top:143px;font-size:16.5px;font-weight:500;color:var(--white);line-height:21px;text-transform:uppercase}

/* section headings */
.section-title{font-size:18px;font-weight:700;color:var(--navy)}
.section-title .accent{color:var(--red)}
.front-heading{left:20px;top:222px}
.underline{left:46px;top:245px;width:35px;height:2px;background:var(--navy)}

/* feature list */
.feature{left:71px;width:445px;font-size:10px;line-height:12.5px}
.feature__name{color:var(--navy);font-weight:500;font-size:10.5px;text-transform:uppercase}
.feature__icon{left:14px;width:42px;display:flex;justify-content:center;color:var(--navy)}
.feature__icon svg{fill:var(--navy)}
.tollfree{font-size:11px;color:var(--navy);font-weight:500}

/* front footer */
.front-footer{left:0;top:618px;width:530px;height:68px;background:var(--navy);display:flex;justify-content:space-around;align-items:center;color:var(--white);font-size:8.5px}
.contact{display:flex;flex-direction:column;align-items:center;gap:8px}
.contact svg{fill:none;stroke:currentColor;stroke-width:1.6}
.social-sq{width:16px;height:16px;background:currentColor;display:block}

/* back */
.city{left:0;top:0;width:530px;height:214px;background:linear-gradient(160deg,#2b2b2b 0%,#5c5c5c 35%,#9a9a9a 60%,#3a3a3a 100%)}
.seat-tab{left:190px;top:0;width:149px;height:44px;background:var(--navy);color:var(--white);font-size:18px;font-weight:500;display:flex;align-items:center;justify-content:center}
.seat-list{list-style:none;font-size:10px;font-weight:500;color:var(--white);line-height:15.8px}
.seat-list li::before{content:"✓";margin-right:6px;font-size:9px}
.seat-list--a{left:108px;top:57px}
.seat-list--b{left:315px;top:57px}
.addon-heading{left:27px;top:220px}

.addon{width:240px;text-align:center;font-size:10px;line-height:12.5px}
.addon svg{display:block;margin:0 auto 4px;fill:none;stroke:var(--navy);stroke-width:2.2}
.addon__name{color:var(--navy);font-weight:700;font-size:10px}

/* pricing table */
.services{left:27px;top:467px;width:478px;border-collapse:collapse;font-size:8px;text-align:center}
.services th,.services td{height:31.5px;padding:0}
.services th{background:var(--navy);color:var(--white);font-weight:500;font-size:8px;line-height:10px;width:119px;border-left:1px solid var(--blue-mid)}
.services th.services__label{background:var(--white);color:var(--navy);font-size:18px;font-weight:700;border:none;height:30px}
.services td.row-label{background:var(--grey-cell);font-weight:500;width:119px}
.services tr.band td.c1{background:var(--blue);color:var(--white)}
.services tr.band td.c2{background:var(--blue-mid);color:var(--white)}
.services tr.band td.c3{background:var(--blue-dark);color:var(--white)}
.services tr.band td.row-label{background:#d2d4d8}

/* back footer */
.back-footer{left:27px;top:640px;width:478px;height:50px;display:flex;align-items:center;justify-content:space-between;color:var(--navy);font-size:6px}
.back-footer .brand{font-size:10px;gap:5px}
.back-footer .brand__mark{width:14px;height:14px}
.back-footer .contact{gap:5px;color:var(--blue-mid)}
.back-footer .contact svg{stroke:var(--navy)}
.back-footer .social-sq{width:11px;height:11px;background:var(--navy)}
</style>
</head>
<body>

<!-- FRONT PAGE -->
<section class="page page--front">
  <div class="abs brand front-brand"><span class="brand__mark"></span>LUMEN BY HARLOW</div>

  <div class="abs hero" role="img" aria-label="Night view of Earth from space with glowing city lights"></div>
  <h1 class="abs hero__title">Clearly Talk</h1>
  <p class="abs hero__sub">Cloud Communications for<br>Your Business</p>

  <h2 class="abs section-title front-heading"><span class="accent">All PBX</span> Include the Following Features:</h2>
  <div class="abs underline"></div>

  <div class="abs feature__icon" style="top:282px">
    <svg width="32" height="40" viewBox="0 0 32 40"><circle cx="16" cy="11" r="8" fill="none" stroke="#0d2d5e" stroke-width="2"/><path d="M2 38c0-9 6-14 14-14s14 5 14 14z" fill="none" stroke="#0d2d5e" stroke-width="2"/></svg>
  </div>
  <div class="abs feature" style="top:266px">
    <div class="feature__name">Auto Attendant</div>
    An automated recording that answers the phone and provides a personalized message to callers with options for connecting to the operator, dialing by name or extension, or connecting to up to nine configurable extensions. Configuration via the Customer Portal allows for hours of operation to be modified, with different options available for hours that the company is open or closed.
  </div>

  <div class="abs feature__icon" style="top:352px">
    <svg width="22" height="38" viewBox="0 0 22 38"><rect x="1.5" y="1.5" width="19" height="35" rx="3" fill="none" stroke="#0d2d5e" stroke-width="2"/><line x1="2" y1="7" x2="20" y2="7" stroke="#0d2d5e" stroke-width="1.5"/><line x1="2" y1="30" x2="20" y2="30" stroke="#0d2d5e" stroke-width="1.5"/></svg>
  </div>
  <div class="abs feature" style="top:353px">
    <div class="feature__name">Company Main Number</div>
    Phone number with unlimited incoming minutes that can be configured to point to any group extension in the PBX (such as an auto attendant or hunt group).
  </div>

  <div class="abs feature__icon tollfree" style="top:420px">+1-800</div>
  <div class="abs feature" style="top:414px">
    <div class="feature__name">Corporate Directory System</div>
    Users are networked for extension to extension calling.
  </div>

  <div class="abs feature__icon" style="top:470px">
    <svg width="40" height="34" viewBox="0 0 40 34"><circle cx="20" cy="7" r="6"/><circle cx="7" cy="11" r="4.5"/><circle cx="33" cy="11" r="4.5"/><path d="M11 34v-10c0-6 4-9 9-9s9 3 9 9v10z"/><path d="M0 34v-9c0-5 3-8 7-8 2 0 3 .5 4 1.5-1 2-1.5 4-1.5 6.5V34z"/><path d="M40 34v-9c0-5-3-8-7-8-2 0-3 .5-4 1.5 1 2 1.5 4 1.5 6.5V34z"/></svg>
  </div>
  <div class="abs feature" style="top:461px">
    <div class="feature__name">Hunt Groups</div>
    Allows users within a group to be included in a specified subgroup to handle incoming calls received by an assigned Hunt Group’s phone number. Within the Customer Portal, company administrators can choose from “hunt” schemes, each of which rings the specified phones in a different manner.
  </div>

  <div class="abs feature__icon" style="top:550px">
    <svg width="24" height="38" viewBox="0 0 24 38"><ellipse cx="8" cy="31" rx="7.5" ry="6"/><rect x="13" y="2" width="3" height="30"/><path d="M16 2c2 6 8 7 8 15-2-5-5-6-8-6z"/></svg>
  </div>
  <div class="abs feature" style="top:549px">
    <div class="feature__name">Music on Hold</div>
    Enables company administrators to upload an audio file (.wav file containing music, advertising, etc.) onto the system to be broadcast to parties while on hold.
  </div>

  <footer class="abs front-footer">
    <div class="contact">
      <svg width="18" height="18" viewBox="0 0 18 18"><circle cx="9" cy="9" r="8"/><ellipse cx="9" cy="9" rx="3.5" ry="8"/><line x1="1" y1="9" x2="17" y2="9"/><path d="M2.5 4.5h13M2.5 13.5h13"/></svg>
      www.lumenbyharlow-example.com
    </div>
    <div class="contact">
      <svg width="18" height="18" viewBox="0 0 18 18" style="fill:currentColor;stroke:none"><path d="M3 1l4 0 1.5 4-2.2 1.6c1 2.2 2.7 3.9 4.9 4.9L12.8 9.3l4 1.5v4c0 1-1 2-2 2C7.5 16.5 1.5 10.5 1 3c0-1 1-2 2-2z"/></svg>
      415.836.0.917
    </div>
    <div class="contact">
      <svg width="22" height="16" viewBox="0 0 22 16"><rect x="1" y="1" width="20" height="14"/><path d="M1 1l10 8 10-8M1 15l7-7M21 15l-7-7"/></svg>
      sales@lumenbyharlow-example.com
    </div>
    <div class="contact">
      <span class="social-sq"></span>
      www.socialsite-example.com/lumenbyharlow
    </div>
  </footer>
</section>

<!-- BACK PAGE -->
<section class="page page--back">
  <div class="abs city" role="img" aria-label="Black and white photo of office skyscrapers seen from below"></div>
  <div class="abs seat-tab">Seat Features:</div>
  <ul class="abs seat-list seat-list--a">
    <li>3-Way Calling</li>
    <li>Call Logs</li>
    <li>Caller ID and Caller Name Delivery</li>
    <li>Call Waiting</li>
    <li>Call Forward Always</li>
    <li>Call Forward Busy</li>
    <li>Call Forward No Answer</li>
    <li>Call Forward Not Reachable</li>
  </ul>
  <ul class="abs seat-list seat-list--b">
    <li>Do Not Disturb</li>
    <li>Extension Dialing</li>
    <li>Last Number Redial</li>
    <li>Simultaneous Ring</li>
    <li>Sequential Ring</li>
    <li>Speed Dial 100</li>
    <li>Unified Messaging</li>
  </ul>

  <h2 class="abs section-title addon-heading"><span class="accent">Add-On</span> Features:</h2>

  <div class="abs addon" style="left:29px;top:250px">
    <svg width="30" height="36" viewBox="0 0 30 36"><circle cx="15" cy="10" r="7.5"/><path d="M2 35c0-8 5.5-13 13-13s13 5 13 13z"/></svg>
    <div class="addon__name">Advanced Auto Attendant</div>
    A multi-level Auto Attendant (for example, enterprise’s main Auto Attendant is configured to seamlessly route to the Auto Attendant of a particular department or location).
  </div>

  <div class="abs addon" style="left:272px;top:250px">
    <svg width="22" height="34" viewBox="0 0 22 34"><rect x="6" y="1.5" width="10" height="19" rx="5"/><path d="M2 14c0 6 4 10 9 10s9-4 9-10M11 24v6M5 32.5h12"/></svg>
    <div class="addon__name">Call Recording</div>
    Allows a user to record their calls in either an always on or ondemand mode. These recording capabilities can allow for personal monitoring or supervised monitoring of recorded calls
  </div>

  <div class="abs addon" style="left:29px;top:362px">
    <svg width="34" height="36" viewBox="0 0 34 36"><path d="M4 20v-4a13 13 0 0 1 26 0v4"/><rect x="2" y="18" width="6" height="10" rx="2" style="fill:#0d2d5e"/><rect x="26" y="18" width="6" height="10" rx="2" style="fill:#0d2d5e"/><path d="M29 28c0 4-4 6-9 6h-3"/></svg>
    <div class="addon__name">Toll-Free Numbers</div>
    An “800” number with inbound calling charged a toll to you, not the caller.
  </div>

  <div class="abs addon" style="left:272px;top:358px">
    <svg width="44" height="32" viewBox="0 0 44 32"><path d="M11 30a9 9 0 0 1-1-18 12 12 0 0 1 23-2 10 10 0 0 1 1 20z"/></svg>
    <div class="addon__name">Virtual Number</div>
    Additional phone number with unlimited incoming minutes that can be configured to point to any extension in the PBX.
  </div>

  <table class="abs services">
    <tr>
      <th class="services__label">SERVICES</th>
      <th>Primer<br>(Location, not a user)</th>
      <th>Standard<br>(Basic user)</th>
      <th>Premium<br>(Power user)</th>
    </tr>
    <tr><td class="row-label">Monthly Price</td><td>$20</td><td>$30</td><td>$35</td></tr>
    <tr class="band"><td class="row-label">Extension Dialing</td><td class="c1">YES</td><td class="c2">YES</td><td class="c3">YES</td></tr>
    <tr><td class="row-label">Call Waiting</td><td>NO</td><td>YES</td><td>YES</td></tr>
    <tr class="band"><td class="row-label">Web Collaboration</td><td class="c1">NO</td><td class="c2">NO</td><td class="c3">YES</td></tr>
  </table>

  <footer class="abs back-footer">
    <div class="brand"><span class="brand__mark"></span>LUMEN BY HARLOW</div>
    <div class="contact">
      <svg width="13" height="13" viewBox="0 0 18 18"><circle cx="9" cy="9" r="8"/><ellipse cx="9" cy="9" rx="3.5" ry="8"/><line x1="1" y1="9" x2="17" y2="9"/></svg>
      www.lumenbyharlow-example.com
    </div>
    <div class="contact">
      <svg width="13" height="13" viewBox="0 0 18 18" style="fill:#0d2d5e;stroke:none"><path d="M3 1l4 0 1.5 4-2.2 1.6c1 2.2 2.7 3.9 4.9 4.9L12.8 9.3l4 1.5v4c0 1-1 2-2 2C7.5 16.5 1.5 10.5 1 3c0-1 1-2 2-2z"/></svg>
      415.836.0.917
    </div>
    <div class="contact">
      <svg width="15" height="11" viewBox="0 0 22 16"><rect x="1" y="1" width="20" height="14"/><path d="M1 1l10 8 10-8"/></svg>
      sales@lumenbyharlow-example.com
    </div>
    <div class="contact">
      <span class="social-sq"></span>
      www.socialsite-example.com/lumenbyharlow
    </div>
  </footer>
</section>

</body>
</html>
```